Beach Polo Event Flyer

The project consists of a flyer for a beach polo event that will occur on August 30 and 31

The flyer should contain the event details in spanish:
IV MARENQUA SHORE RIDING CUP
Hotel Varlowe
Agosto 30 y 31 2014
Horario: 2pm a 6pm
(Varlowe Logo)

Also contact info below:
info@brisadelvarclub.example
www.brisadelvarclub.example

A Space should be left on the bottom for us to add the sponsor logos when we have them.

The general idea is to do a flyer that looks elegant, inviting, inspired on the beach and the caribbean and shows the beauty of the sport and the beach.

I am attaching the flyer that a friend made that we DO NOT LIKE and some flyers from events in other parts of the world that we do like.
Also attached you will find the BRISADEL VAR CLUB logo which should go somewhere in the flyer. We are also attaching pictures from the past event in case you would need to use them.
We are open for any questions

```html
<!DOCTYPE html>
<html lang="es">
<head>
<meta charset="utf-8">
<title>IV Marenqua Shore Riding Cup</title>
<link rel="stylesheet" href="https://fonts.googleapis.com/css2?family=Cinzel:wght@400;600&family=Cormorant+Garamond:wght@500;600&display=swap">
<style>
  :root {
    --navy: #1f3557;
    --navy-deep: #18294a;
    --gold: #b99a52;
    --sand: #efe6d2;
    --sand-warm: #e4d6b8;
    --sky-top: #2a78d2;
    --sky-low: #8fc6ee;
    --sea: #35c2cf;
    --sea-light: #9fe3e3;
    --white: #ffffff;
  }
  * { margin: 0; padding: 0; box-sizing: border-box; }
  html, body { width: 849px; height: 1200px; overflow: hidden; background: var(--white); }
  .flyer {
    position: relative;
    width: 849px;
    height: 1200px;
    overflow: hidden;
    background: var(--sand);
    font-family: "Cormorant Garamond", Georgia, serif;
  }
  .beach-photo {
    position: absolute;
    top: 0;
    left: 0;
    width: 100%;
    height: 720px;
    background: linear-gradient(180deg,
      var(--sky-top) 0%,
      var(--sky-low) 38%,
      #d8eef7 44%,
      var(--sea) 46%,
      var(--sea-light) 56%,
      var(--sand-warm) 70%,
      var(--sand) 100%);
  }
  .club-badge {
    position: absolute;
    top: 0;
    left: 594px;
    width: 210px;
    height: 212px;
    background: var(--navy);
    display: flex;
    flex-direction: column;
    align-items: center;
    justify-content: center;
    gap: 18px;
  }
  .club-badge .mark {
    width: 66px;
    height: 66px;
    border-radius: 50%;
    background: var(--gold);
  }
  .club-badge .name {
    font-family: "Cinzel", Georgia, serif;
    font-weight: 600;
    font-size: 19px;
    letter-spacing: 1px;
    color: var(--gold);
    text-align: center;
    line-height: 1.1;
  }
  .event-title {
    position: absolute;
    top: 732px;
    left: 0;
    width: 100%;
    text-align: center;
    font-family: "Cinzel", Georgia, serif;
    font-weight: 600;
    font-size: 58px;
    line-height: 70px;
    color: var(--navy);
    letter-spacing: 1px;
  }
  .event-date {
    position: absolute;
    top: 894px;
    left: 0;
    width: 100%;
    display: flex;
    align-items: center;
    justify-content: center;
    gap: 18px;
    font-family: "Cinzel", Georgia, serif;
    font-weight: 600;
    font-size: 24px;
    color: var(--gold);
    letter-spacing: 2px;
  }
  .event-date .rule { width: 112px; height: 2px; background: var(--gold); }
  .venue {
    position: absolute;
    top: 952px;
    left: 0;
    width: 100%;
    display: flex;
    justify-content: center;
    align-items: center;
  }
  .venue .details {
    text-align: left;
    font-size: 29px;
    line-height: 34px;
    font-weight: 500;
    color: var(--navy);
    padding-right: 22px;
  }
  .venue .divider { width: 2px; height: 76px; background: var(--gold); }
  .venue .host {
    padding-left: 24px;
    display: flex;
    align-items: center;
    gap: 10px;
    font-size: 32px;
    font-weight: 600;
    color: var(--navy);
  }
  .venue .host .mark { width: 20px; height: 20px; border-radius: 50%; background: var(--navy); }
  .sponsor-space {
    position: absolute;
    left: 60px;
    top: 1040px;
    width: 729px;
    height: 108px;
  }
  .contact-bar {
    position: absolute;
    left: 0;
    bottom: 0;
    width: 100%;
    height: 39px;
    background: var(--navy-deep);
    color: var(--white);
    font-size: 18px;
    display: flex;
    align-items: center;
    justify-content: center;
    letter-spacing: 0.5px;
  }
</style>
</head>
<body>
  <div class="flyer">
    <div class="beach-photo" role="img" aria-label="Photo of polo players on horseback galloping on a Caribbean beach under a blue sky, turquoise sea behind"></div>

    <div class="club-badge">
      <div class="mark"></div>
      <div class="name">BRISADEL VAR<br>CLUB</div>
    </div>

    <h1 class="event-title">IV MARENQUA<br>SHORE RIDING CUP</h1>

    <div class="event-date">
      <span class="rule"></span>
      <span>AGOSTO 30 Y 31 2014</span>
      <span class="rule"></span>
    </div>

    <div class="venue">
      <div class="details">at Hotel Varlowe<br>Horario 2pm a 6pm</div>
      <div class="divider"></div>
      <div class="host"><span class="mark"></span>Varlowe</div>
    </div>

    <div class="sponsor-space" aria-label="Reserved space for sponsor logos"></div>

    <div class="contact-bar">info@brisadelvarclub.example &nbsp;|&nbsp; www.brisadelvarclub.example</div>
  </div>
</body>
</html>
```